Lorna Tess Tresses Fancy Business Card’s

I want my business cards to be elite, original and very classy. I want the business cards to match the colors of my logo and to match the design posted. I would love the design of the picture I posted

I want the card all white .
The dripping on the top of the card I want it to match the pink color in my logo that’s also posted .
I need my logo on the business card !
I need my Instagram- @lorna.tess.tresses__
And my phone number - 582 907 3365

Target Market(s)

My target market is young woman age 23 to older woman to the age of 65
I want both older and younger women to love my design . I don’t want any cheap looking business cards

Industry/Entity Type

Hair And Beauty

Contact Information for Business Card

Add my logo
Add my Instagram- @lorna.tess.tresses__
My number - 582 907 3365
My website- www.lornatesstresses.example

Font styles to use
Serif
Script

Colors
ffffff
e667a6
e34298

Requirements
Must have
• The business cards must have my logo, my number , my website, and my Instagram!
Nice to have
• Nice to have glitter words that match my logo
• The business cards must look classy and mature
• I want them to be very unique!!
Should not have
• Should not have any colors that doesn’t match my logo ! This is very important! Please

```html
<!DOCTYPE html>
<html lang="en">
<head>
<meta charset="utf-8">
<title>Lorna Tess Tresses — Business Card</title>
<link rel="stylesheet" href="https://fonts.googleapis.com/css2?family=Raleway:wght@500;600&family=Roboto:wght@400&display=swap">
<style>
  :root {
    --pink: #e34298;
    --pink-soft: #e667a6;
    --white: #ffffff;
    --ink: #3a3a3a;
    --card-dark: #1c1b1c;
    --backdrop: #eeeeee;
  }
  * { box-sizing: border-box; margin: 0; padding: 0; }
  html, body { width: 1200px; height: 800px; overflow: hidden; }
  body { background: var(--backdrop); position: relative; font-family: "Roboto", Arial, sans-serif; }

  .card { position: absolute; width: 571px; height: 330px; }
  .card--front { left: 475px; top: 31px; background: var(--white); }
  .card--back { left: 170px; top: 404px; background: var(--card-dark); }

  .brand-mark {
    font-family: "Raleway", Arial, sans-serif;
    font-weight: 600;
    color: var(--pink);
    line-height: 1.05;
    letter-spacing: 0.02em;
  }
  .card--front .brand-mark {
    position: absolute; right: 52px; top: 52px;
    font-size: 30px; text-align: right;
  }
  .card--back .brand-mark {
    position: absolute; left: 0; right: 0; top: 50%;
    transform: translateY(-50%);
    font-size: 44px; text-align: center;
  }

  .holder { position: absolute; left: 51px; top: 126px; }
  .holder__name {
    font-family: "Raleway", Arial, sans-serif; font-weight: 600;
    font-size: 22px; color: var(--pink);
  }
  .holder__role { font-size: 15px; color: var(--ink); margin-top: 4px; }

  .contact-list { position: absolute; left: 51px; top: 198px; list-style: none; }
  .contact-list li {
    display: flex; align-items: center; gap: 7px;
    font-size: 15.5px; color: var(--ink); height: 21.5px;
  }
  .contact-list svg { width: 14px; height: 14px; flex: none; }
</style>
</head>
<body>
  <section class="card card--front" aria-label="Business card front">
    <div class="brand-mark">Lorna<br>Tess<br>Tresses</div>

    <div class="holder">
      <p class="holder__name">Lorna tess tresses</p>
      <p class="holder__role">Managing Director</p>
    </div>

    <ul class="contact-list">
      <li>
        <svg viewBox="0 0 16 16" aria-hidden="true"><path fill="var(--pink)" d="M3.6 1.5l2.3 2.6-1.2 1.8c.9 2 2.6 3.7 4.6 4.6l1.8-1.2 2.6 2.3-1.4 2.1C7.2 13.6 2.4 8.8 1.5 3z"/></svg>
        582 907 3365
      </li>
      <li>
        <svg viewBox="0 0 16 16" aria-hidden="true"><rect x="1" y="3" width="14" height="10" fill="var(--pink)"/><path d="M1.5 3.5L8 9l6.5-5.5" stroke="#fff" stroke-width="1.3" fill="none"/></svg>
        info@lornatesstresses.example
      </li>
      <li>
        <svg viewBox="0 0 16 16" aria-hidden="true"><circle cx="8" cy="8" r="6.5" fill="var(--pink)"/><path d="M1.5 8h13M8 1.5c-3 3.5-3 9.5 0 13M8 1.5c3 3.5 3 9.5 0 13" stroke="#fff" stroke-width="1" fill="none"/></svg>
        www.lornatesstresses.example
      </li>
      <li>
        <svg viewBox="0 0 16 16" aria-hidden="true"><rect x="1.5" y="1.5" width="13" height="13" rx="2" fill="var(--pink)"/></svg>
        @lorna.tess.tresses__
      </li>
    </ul>
  </section>

  <section class="card card--back" aria-label="Business card back">
    <div class="brand-mark">Lorna<br>Tess Tresses</div>
  </section>
</body>
</html>
```